Veltaro Resident Safety and Security

Need a website for our company. Please see attached outlines and files
Main Page
Veltaro
Design – Install – Maintain
Supporting the Safety and Security needs of your Community
Best in Class Systems for the Safety and Security of your Residents and Staff
Your Trusted Advisor
Solutions
Systems tailored to the needs of your facility
Skilled Nursing Facilities
Long Term Care
CCRC’s
Assisted Living
Independent Living
Access Control
Maglocks
Keypads
Prox readers (key fob, card, etc.)
Wireless locks
Multi-Tennant
Perimeter doors
Resident Apartment doors
Nurse Call
Tone / Visual
Fixed Stations
Dome Lights
T/V+ Audio
Fixed Stations
Dome Lights
Audio communication
Wireless
Fixed Stations
Resident Pendants
Hybrid Systems
Wired and Wireless integrated for seamless notification and reporting.
CCTV
Surveillance systems to fit your security needs and your budget
Remote Access, Local or Cloud Storage
Good, Better, Best proposals
Wander management
Door Alarming
Detection of wandering resident
Remote alarming and alerts
Delay elopement to allow for redirection
Network Infrastructure
Modern infrastructure for modern systems
Conference and Telepresence
Professionally installed systems to allow for seamless clear communications between teams across infinite distances.
Our Team
Mark Dunleavy – President
Paula Hobart – Vice President of Customer Success
Colin Marsh – Account Executive
Industry Associations
Granite Harbor Guild
Massachusetts chapter of the National Guild of Care Facility Stewards
Contact Us
Phone (603) 555-0172
Email Info@Veltaro-example.com
Facilities we serve
Independent Senior Living
Assisted Living
Memory Care
CCRC (Continuing Care Retirement Community)
Skilled Nursing / Rehab
Multi-Tenant
Outpatient Surgical Centers
Endoscopy Clinics
Acute Care
Urgent Care
Commercial Properties of all types
General notes
Imagery should invoke high tech, safety, security and include healthcare themes. the circuit board shield is our logo and a ghosted image as back ground or some animation that brings in the logo or the circuit board should be incorporated.
Veltaro is a systems integration company specializing in low voltage solutions for healthcare facilities and senior living communities. The company aims to leverage its industry expertise, and innovative products to become the market leader in systems integration, focusing on enhancing safety and operational efficiency.
Vision and Mission: Veltaro’s vision is to revolutionize integrated systems within healthcare and commercial environments by delivering innovative, reliable, and tailored solutions that enhance operational efficiency and patient care. The company is committed to setting new standards for resident safety and customer satisfaction.
Company Summary: Founded by experienced industry professionals, Veltaro specializes in the design, installation, and maintenance of systems including Access Control, Nurse Call, Delayed Egress, network infrastructure, and overhead paging primarily for healthcare clients.
Products and Services: The company offers a comprehensive range of low voltage systems including Nurse Call (wired and wireless), Wander Management, Access Control, and wired/wireless network infrastructure tailored for senior living and healthcare facilities.
Mission Statement
Veltaro was founded to fill a specific need. Senor living communities and healthcare facilities of all kinds face unique challenges in regards to technology and systems integration. Veltaro is perfectly positioned with an experienced management team, skilled technicians, industry relationships with suppliers and facility management groups. We have built our reputation on excellent customer service and the highest standards of integrity. Veltaro’s vision is to revolutionize integrated systems within healthcare and commercial environments by delivering innovative, reliable, and tailored solutions that enhance operational efficiency and patient care. We are committed to setting new standards for resident safety and customer satisfaction in every project we undertake.

Target Market(s)

Senior living communities staff and management

Industry/Entity Type

Systems Intergration

Coding

Coded - Design and coding required

Font styles to use
Serif
Sans Serif

Colors
0054AA
0677BA
7BADD7
CADEEF
E8F1F8
0094D4
00A9DD
6FCCEA
C7EBF8
E9F6FB

Requirements
Must have
• unique eye catching design including circuit board (PCB) type design and our supplied logo files

```html
<!DOCTYPE html>
<html lang="en">
<head>
<meta charset="utf-8">
<title>Veltaro Resident Safety and Security</title>
<link href="https://fonts.googleapis.com/css2?family=Noto+Serif:wght@400;500&family=Inter:wght@400;500;600&display=swap" rel="stylesheet">
<style>
:root{
  --blue-deep:#0054AA;
  --blue-mid:#0677BA;
  --blue-soft:#7BADD7;
  --blue-pale:#CADEEF;
  --blue-mist:#E8F1F8;
  --cyan:#0094D4;
  --cyan-bright:#00A9DD;
  --cyan-soft:#6FCCEA;
  --cyan-pale:#C7EBF8;
  --cyan-mist:#E9F6FB;
  --ink:#1b1f2a;
  --text:#3a3f4a;
  --white:#ffffff;
  --serif:"Noto Serif", Georgia, serif;
  --sans:"Inter", Arial, sans-serif;
}
*{box-sizing:border-box;margin:0;padding:0}
html,body{width:1200px;height:3138px;overflow:hidden;background:var(--white)}
body{font-family:var(--sans);color:var(--text);position:relative}
a{color:inherit;text-decoration:none}
.abs{position:absolute}
section,header,footer{position:absolute;left:0;width:1200px}

/* buttons */
.btn{position:absolute;display:flex;align-items:center;justify-content:center;border:2px solid var(--blue-mid);border-radius:20px;font-size:10.5px;letter-spacing:.8px;text-transform:uppercase;color:var(--blue-mid);background:var(--white);box-shadow:0 2px 6px rgba(0,84,170,.15)}
.btn-round{position:absolute;width:32px;height:32px;border-radius:50%;border:2px solid var(--blue-mid);display:flex;align-items:center;justify-content:center;background:var(--white)}
.btn-round.filled{background:var(--blue-deep);border-color:var(--blue-pale)}
.social{position:absolute;width:30px;height:30px;border-radius:50%;border:1.5px solid var(--blue-mid);background:var(--white)}
.social.active{background:var(--blue-deep);border-color:var(--blue-pale)}
.social::after{content:"";position:absolute;left:50%;top:50%;width:8px;height:8px;margin:-4px 0 0 -4px;border-radius:50%;background:var(--blue-deep)}
.social.active::after{background:var(--white)}

/* header */
.site-header{top:0;height:105px;background:var(--white);z-index:5}
.logo-bulge{position:absolute;left:165px;top:40px;width:200px;height:110px;border-radius:0 0 100px 100px;background:var(--white);z-index:6}
.logo{position:absolute;left:200px;top:12px;width:130px;z-index:7;display:flex;flex-direction:column;align-items:center}
.logo-mark{width:62px;height:62px;border-radius:50%;background:var(--cyan)}
.logo-name{font-family:var(--serif);font-size:24px;color:var(--blue-deep);margin-top:10px;letter-spacing:.5px}
.topbar{position:absolute;top:20px;font-size:11px;color:var(--ink);display:flex;align-items:center;gap:6px}
.topbar.email{color:var(--blue-mid);text-decoration:underline}
.follow-label{position:absolute;left:796px;top:23px;font-size:9px;font-weight:600;letter-spacing:.8px;color:var(--blue-deep)}
.nav{position:absolute;top:68px;left:408px;display:flex;font-size:9.5px;letter-spacing:.4px;text-transform:uppercase;color:var(--ink)}
.nav a{position:absolute;white-space:nowrap}
.nav a.current{color:var(--blue-mid)}
.nav a.current::after{content:"";position:absolute;left:0;right:0;top:17px;height:2px;background:var(--blue-mid)}
.caret{display:inline-block;width:5px;height:5px;border-right:1px solid currentColor;border-bottom:1px solid currentColor;transform:rotate(45deg);margin-left:5px;position:relative;top:-2px}

/* hero */
.hero{top:105px;height:469px;background:linear-gradient(90deg,#0a4c9e 0%,#08306a 35%,#030d1e 62%,#000 100%)}
.hero-visual{position:absolute;left:520px;top:0;width:680px;height:469px;background:radial-gradient(circle at 38% 45%,rgba(0,169,221,.55) 0,rgba(0,148,212,.25) 22%,rgba(0,0,0,0) 50%),radial-gradient(circle at 85% 25%,rgba(60,90,180,.5) 0,rgba(0,0,0,0) 30%)}
.hero-title{position:absolute;left:199px;top:125px;font-family:var(--serif);font-size:29px;line-height:37px;color:var(--white);text-transform:uppercase;letter-spacing:.5px}
.hero-sub{position:absolute;left:199px;top:249px;font-size:11.5px;line-height:18px;color:var(--white)}
.hero .btn{top:304px;height:32px}
.hero .btn.ghost{background:transparent;border-color:var(--white);color:var(--white);box-shadow:none}
.scroll-cue{position:absolute;left:977px;top:403px;width:24px;height:40px;border:2px solid var(--white);border-radius:12px}

/* about */
.about{top:574px;height:477px;background:linear-gradient(180deg,#fff 0%,var(--blue-mist) 100%)}
.eyebrow{position:absolute;font-size:9px;font-weight:600;letter-spacing:2px;color:var(--blue-mid);text-transform:uppercase}
.about-title{position:absolute;left:627px;top:138px;font-family:var(--serif);font-size:28px;line-height:34px;color:var(--ink);text-transform:uppercase}
.about-title span{color:var(--blue-mid)}
.about-title small{font-size:8px;color:var(--blue-mid)}
.rule{position:absolute;height:1.5px;background:var(--blue-mid)}
.about-text{position:absolute;left:627px;top:230px;width:380px;font-size:11px;line-height:19px;color:var(--text)}
.about-text b{color:var(--ink);font-weight:600}

/* solutions */
.solutions{top:1051px;height:419px;background:linear-gradient(180deg,#d9e8f2 0%,#dbe9f2 70%,#cfe1ee 100%);overflow:hidden}
.solutions-glow{position:absolute;left:580px;top:0;width:560px;height:419px;background:radial-gradient(circle at 45% 45%,rgba(255,255,255,.55) 0,rgba(255,255,255,0) 60%)}
.section-title{position:absolute;left:0;width:1200px;text-align:center;font-family:var(--serif);font-size:27px;color:var(--ink);text-transform:uppercase}
.section-title span{color:var(--blue-mid)}
.solution{position:absolute;top:121px;width:160px;text-align:center}
.solution svg{display:block;margin:0 auto}
.solution p{margin-top:16px;font-size:12.5px;line-height:16px;color:var(--ink)}
.solutions .btn{top:326px;width:88px;height:32px;left:556px}

/* team */
.team{top:1470px;height:458px;background:var(--white)}
.member{position:absolute;top:119px;width:220px;text-align:center}
.member-photo{width:190px;height:190px;margin:0 auto;border-radius:50%;border-right:2px solid var(--blue-mid);border-bottom:2px solid var(--blue-mid)}
.member-name{font-family:var(--serif);font-size:21px;color:var(--blue-mid);margin-top:14px}
.member-rule{width:60px;height:1.5px;background:var(--blue-soft);margin:10px auto 0}
.member-role{font-size:10px;letter-spacing:1.3px;text-transform:uppercase;color:var(--ink);margin-top:14px;line-height:15px}

/* facilities */
.facilities{top:1928px;height:429px;background:linear-gradient(180deg,var(--blue-mist) 0%,#fff 60%)}
.facility{position:absolute;top:119px;width:254px;height:192px;border-radius:6px;overflow:hidden}
.facility-img{position:absolute;inset:0}
.facility-shade{position:absolute;left:0;right:0;bottom:0;height:90px;background:linear-gradient(180deg,rgba(0,84,170,0),rgba(0,84,170,.9))}
.facility-label{position:absolute;left:17px;bottom:18px;font-size:12.5px;font-weight:500;color:var(--white)}

/* vision */
.vision{top:2357px;height:485px;background:#f7f9fb}
.vision-title{position:absolute;left:219px;top:132px;font-family:var(--serif);font-size:27px;color:var(--ink);text-transform:uppercase}
.vision-title span{color:var(--blue-mid)}
.vision-text{position:absolute;left:219px;top:196px;width:380px;font-size:11px;line-height:19px}
.vision-text b{color:var(--ink);font-weight:600}

/* footer */
.site-footer{top:2842px;height:296px;background:var(--blue-deep);color:var(--white)}
.footer-title{position:absolute;top:28px;font-family:var(--serif);font-size:18.5px}
.footer-title span{color:var(--cyan-soft)}
.contact-line{position:absolute;left:199px;display:flex;gap:10px;font-size:12px;line-height:14px;align-items:flex-start}
.contact-line svg{flex:none}
.footer-links{position:absolute;left:472px;top:76px;list-style:none;font-size:11.5px;line-height:21.3px}
.footer-links a.current{text-decoration:underline}
.field{position:absolute;background:#1566bb;border-radius:14px;font-size:10px;color:var(--white);padding:9px 12px}
.site-footer .social{border-color:var(--white);background:transparent}
.site-footer .social::after{background:var(--white)}
.site-footer .social.active{background:var(--cyan)}
.submit{position:absolute;left:911px;top:199px;width:89px;height:32px;border:2px solid var(--white);border-radius:18px;display:flex;align-items:center;justify-content:center;font-size:10.5px;letter-spacing:.8px}
.copyright{position:absolute;left:0;top:262px;width:1200px;height:34px;background:var(--cyan);font-size:9.5px;padding:13px 0 0 199px}
.copyright u{text-decoration:underline}
</style>
</head>
<body>

<header class="site-header">
  <div class="logo-bulge"></div>
  <a class="logo" href="#" aria-label="Veltaro home">
    <span class="logo-mark"></span>
    <span class="logo-name">Veltaro</span>
  </a>
  <div class="topbar" style="left:481px">
    <svg width="12" height="12" viewBox="0 0 24 24" fill="none" stroke="#0054AA" stroke-width="2"><path d="M5 3h4l2 5-3 2a11 11 0 0 0 6 6l2-3 5 2v4a2 2 0 0 1-2 2A17 17 0 0 1 3 5a2 2 0 0 1 2-2z"/></svg>
    (603) 555-0172
  </div>
  <div class="topbar email" style="left:603px">
    <svg width="12" height="12" viewBox="0 0 24 24" fill="none" stroke="#0054AA" stroke-width="2"><rect x="3" y="5" width="18" height="14" rx="2"/><path d="M3 7l9 6 9-6"/></svg>
    Info@Veltaro-example.com
  </div>
  <span class="follow-label">FOLLOW US:</span>
  <span class="social" style="left:864px;top:14px" aria-label="Social link"></span>
  <span class="social active" style="left:900px;top:14px" aria-label="Social link"></span>
  <span class="social" style="left:934px;top:14px" aria-label="Social link"></span>
  <span class="social" style="left:969px;top:14px" aria-label="Social link"></span>
  <nav class="nav">
    <a class="current" style="left:0" href="#">Home</a>
    <a style="left:55px" href="#">About</a>
    <a style="left:110px" href="#">Solutions<i class="caret"></i></a>
    <a style="left:202px" href="#">Our Services<i class="caret"></i></a>
    <a style="left:314px" href="#">We Serve<i class="caret"></i></a>
    <a style="left:405px" href="#">Industry</a>
  </nav>
  <a class="btn" href="#" style="left:893px;top:58px;width:107px;height:32px">Contact Us</a>
</header>

<section class="hero">
  <div class="hero-visual" role="img" aria-label="Hand touching a glowing digital padlock surrounded by circuit rings and healthcare icons"></div>
  <h1 class="hero-title">Supporting the safety<br>and security needs of<br>your community</h1>
  <p class="hero-sub">Best in Class Systems for the Safety and Security of your<br>Residents and Staff.</p>
  <a class="btn" href="#" style="left:199px;width:107px">Contact Us</a>
  <a class="btn ghost" href="#" style="left:318px;width:107px">Call Now!</a>
  <div class="scroll-cue"><svg width="20" height="36" viewBox="0 0 20 36" fill="none" stroke="#fff" stroke-width="1.5"><path d="M10 9v18M6 23l4 4 4-4"/></svg></div>
</section>

<section class="about">
  <svg class="abs" style="left:219px;top:57px" width="354" height="364" viewBox="0 0 100 103" role="img" aria-label="Caregiver talking with an older resident in a bright hallway">
    <defs><linearGradient id="aboutFill" x1="0" y1="0" x2="1" y2="1"><stop offset="0" stop-color="#9fb8a8"/><stop offset=".5" stop-color="#c9cfd3"/><stop offset="1" stop-color="#6d7f8f"/></linearGradient></defs>
    <path d="M50 1.5C62 11 80 16 97 19L96 55C94 78 74 94 50 101.5C26 94 6 78 4 55L3 19C20 16 38 11 50 1.5Z" fill="url(#aboutFill)" stroke="#0054AA" stroke-width="1"/>
  </svg>
  <span class="eyebrow" style="left:627px;top:119px">About Us</span>
  <h2 class="about-title">Welcome to the<br><span>Veltaro</span> <small>LLC</small></h2>
  <span class="rule" style="left:609px;top:215px;width:61px"></span>
  <p class="about-text">Founded by experienced industry professionals, <b>Veltaro</b> specializes in the design, installation, and maintenance of systems including Access Control, Nurse Call, Delayed Egress, network infrastructure, and overhead paging primarily for healthcare clients.</p>
  <a class="btn" href="#" style="left:627px;top:327px;width:120px;height:32px">Explore More</a>
</section>

<section class="solutions">
  <div class="solutions-glow"></div>
  <h2 class="section-title" style="top:56px">Solutions</h2>

  <div class="solution" style="left:193px">
    <svg width="118" height="118" viewBox="0 0 100 100"><path d="M50 2C62 10 80 14 96 14L96 50C96 75 75 92 50 100C25 92 4 75 4 50L4 14C20 14 38 10 50 2Z" fill="#fff" stroke="#0677BA" stroke-width="1.5"/><g fill="none" stroke="#0054AA" stroke-width="1.6"><rect x="28" y="34" width="24" height="34"/><path d="M33 42h5M42 42h5M33 50h5M42 50h5M36 68v-8h8v8"/><circle cx="38" cy="26" r="5"/><path d="M38 23v6M35 26h6"/><circle cx="62" cy="42" r="5"/><path d="M54 68c0-10 3-16 8-16s8 6 8 16z"/></g></svg>
    <p>Systems Tailored To<br>The Needs Of Your<br>Facility</p>
  </div>
  <div class="solution" style="left:356px">
    <svg width="118" height="118" viewBox="0 0 100 100"><path d="M50 2C62 10 80 14 96 14L96 50C96 75 75 92 50 100C25 92 4 75 4 50L4 14C20 14 38 10 50 2Z" fill="#fff" stroke="#0677BA" stroke-width="1.5"/><g fill="none" stroke="#0054AA" stroke-width="1.6"><path d="M44 26c6 4 12 5 18 5v12c0 10-8 16-18 19-10-3-18-9-18-19V31c6 0 12-1 18-5z"/><path d="M37 44l5 5 9-9"/><rect x="56" y="48" width="12" height="20" rx="2"/><path d="M59 54h6M59 59h6"/></g></svg>
    <p>Skilled Nursing<br>Facilities</p>
  </div>
  <div class="solution" style="left:519px">
    <svg width="118" height="118" viewBox="0 0 100 100"><path d="M50 2C62 10 80 14 96 14L96 50C96 75 75 92 50 100C25 92 4 75 4 50L4 14C20 14 38 10 50 2Z" fill="#fff" stroke="#0677BA" stroke-width="1.5"/><g fill="none" stroke="#0054AA" stroke-width="1.6"><rect x="28" y="26" width="20" height="16" rx="2"/><path d="M32 31h12M32 36h8"/><path d="M30 50h6l2 5-3 2a9 9 0 0 0 5 5l2-3 5 2v5c-12 0-19-8-19-16z"/><circle cx="62" cy="40" r="6"/><path d="M52 68c0-10 4-16 10-16s10 6 10 16z"/><path d="M62 28v6M59 31h6"/></g></svg>
    <p>Nurse Call</p>
  </div>
  <div class="solution" style="left:682px">
    <svg width="118" height="118" viewBox="0 0 100 100"><path d="M50 2C62 10 80 14 96 14L96 50C96 75 75 92 50 100C25 92 4 75 4 50L4 14C20 14 38 10 50 2Z" fill="#fff" stroke="#0677BA" stroke-width="1.5"/><g fill="none" stroke="#0054AA" stroke-width="1.6"><path d="M50 44c-5-6-8-10-8-14a8 8 0 0 1 16 0c0 4-3 8-8 14z"/><circle cx="50" cy="30" r="3"/><circle cx="34" cy="50" r="6"/><path d="M34 47v3h3"/><circle cx="66" cy="50" r="6"/><circle cx="66" cy="50" r="2"/><circle cx="50" cy="58" r="4"/><path d="M42 70c0-5 3-8 8-8s8 3 8 8z"/></g></svg>
    <p>Wander<br>management</p>
  </div>
  <div class="solution" style="left:846px">
    <svg width="118" height="118" viewBox="0 0 100 100"><path d="M50 2C62 10 80 14 96 14L96 50C96 75 75 92 50 100C25 92 4 75 4 50L4 14C20 14 38 10 50 2Z" fill="#fff" stroke="#0677BA" stroke-width="1.5"/><g fill="none" stroke="#0054AA" stroke-width="1.6"><rect x="36" y="24" width="28" height="9" rx="1"/><rect x="36" y="37" width="28" height="9" rx="1"/><rect x="36" y="50" width="28" height="9" rx="1"/><path d="M50 59v8M36 67h28M30 28h6M64 28h6M30 54h6M64 54h6"/><circle cx="28" cy="28" r="2"/><circle cx="72" cy="28" r="2"/><circle cx="28" cy="54" r="2"/><circle cx="72" cy="54" r="2"/></g></svg>
    <p>Network<br>Infrastructure</p>
  </div>

  <a class="btn-round" href="#" style="left:511px;top:324px" aria-label="Previous"><svg width="14" height="10" viewBox="0 0 14 10" fill="none" stroke="#0677BA" stroke-width="1.3"><path d="M13 5H1M5 1L1 5l4 4"/></svg></a>
  <a class="btn" href="#">View All</a>
  <a class="btn-round filled" href="#" style="left:655px;top:324px" aria-label="Next"><svg width="14" height="10" viewBox="0 0 14 10" fill="none" stroke="#fff" stroke-width="1.3"><path d="M1 5h12M9 1l4 4-4 4"/></svg></a>
</section>

<section class="team">
  <h2 class="section-title" style="top:55px">Our <span>Team</span> Members</h2>
  <span class="rule" style="left:570px;top:92px;width:60px;background:var(--blue-soft)"></span>
  <div class="member" style="left:246px">
    <div class="member-photo" role="img" aria-label="Portrait of Mark Dunleavy" style="background:radial-gradient(circle at 50% 40%,#d8b7a0 0,#a26d5a 55%,#6e4538 100%)"></div>
    <div class="member-name">Mark Dunleavy</div><div class="member-rule"></div>
    <div class="member-role">President</div>
  </div>
  <div class="member" style="left:489px">
    <div class="member-photo" role="img" aria-label="Portrait of Paula Hobart" style="background:radial-gradient(circle at 50% 40%,#4d7dc6 0,#1e55aa 60%,#0e3f8e 100%)"></div>
    <div class="member-name">Paula Hobart</div><div class="member-rule"></div>
    <div class="member-role">Vice President of Customer<br>Success</div>
  </div>
  <div class="member" style="left:728px">
    <div class="member-photo" role="img" aria-label="Portrait of Colin Marsh" style="background:linear-gradient(180deg,#c9a63a 0,#8a7a52 40%,#e9ecef 75%,#d4d8dc 100%)"></div>
    <div class="member-name">Colin Marsh</div><div class="member-rule"></div>
    <div class="member-role">Account Executive</div>
  </div>
</section>

<section class="facilities">
  <h2 class="section-title" style="top:55px">Facilities We <span>Serve</span></h2>
  <span class="rule" style="left:570px;top:94px;width:60px;background:var(--blue-soft)"></span>
  <div class="facility" style="left:200px">
    <div class="facility-img" role="img" aria-label="Older man playing chess in a bright lounge" style="background:linear-gradient(135deg,#e6e2da 0,#b7ab98 45%,#6f6a62 100%)"></div>
    <div class="facility-shade"></div><span class="facility-label">Independent Senior Living</span>
  </div>
  <div class="facility" style="left:473px">
    <div class="facility-img" role="img" aria-label="Nurse assisting a resident seated in a wheelchair" style="background:linear-gradient(135deg,#7c6a55 0,#b9b4ad 45%,#5d6f8f 100%)"></div>
    <div class="facility-shade"></div><span class="facility-label">Assisted Living</span>
  </div>
  <div class="facility" style="left:744px">
    <div class="facility-img" role="img" aria-label="Carer and resident solving a puzzle together" style="background:linear-gradient(135deg,#d7cbbd 0,#a8a195 45%,#6f8096 100%)"></div>
    <div class="facility-shade"></div><span class="facility-label">Memory Care</span>
  </div>
  <a class="btn-round" href="#" style="left:511px;top:335px" aria-label="Previous"><svg width="14" height="10" viewBox="0 0 14 10" fill="none" stroke="#0677BA" stroke-width="1.3"><path d="M13 5H1M5 1L1 5l4 4"/></svg></a>
  <a class="btn" href="#" style="left:556px;top:335px;width:88px;height:32px;background:var(--blue-deep);color:#fff;border-color:var(--blue-pale)">View All</a>
  <a class="btn-round" href="#" style="left:655px;top:335px" aria-label="Next"><svg width="14" height="10" viewBox="0 0 14 10" fill="none" stroke="#0677BA" stroke-width="1.3"><path d="M1 5h12M9 1l4 4-4 4"/></svg></a>
</section>

<section class="vision">
  <h2 class="vision-title">Vision and <span>Mission</span></h2>
  <span class="rule" style="left:200px;top:179px;width:62px"></span>
  <p class="vision-text"><b>Veltaro’s</b> vision is to revolutionize integrated systems within healthcare and commercial environments by delivering innovative, reliable, and tailored solutions that enhance operational efficiency and patient care. The company is committed to setting new standards for resident safety and customer satisfaction.</p>
  <a class="btn" href="#" style="left:219px;top:322px;width:120px;height:32px">Explore More</a>
  <svg class="abs" style="left:630px;top:61px" width="352" height="362" viewBox="0 0 100 103" role="img" aria-label="Therapist guiding an older man in a wheelchair through a dumbbell exercise">
    <defs><linearGradient id="visionFill" x1="0" y1="0" x2="1" y2="1"><stop offset="0" stop-color="#c7a58f"/><stop offset=".5" stop-color="#8f8294"/><stop offset="1" stop-color="#3d4763"/></linearGradient></defs>
    <path d="M50 1.5C62 11 80 16 97 19L96 55C94 78 74 94 50 101.5C26 94 6 78 4 55L3 19C20 16 38 11 50 1.5Z" fill="url(#visionFill)"/>
    <path d="M97 19L96 55C94 78 74 94 50 101.5" fill="none" stroke="#0054AA" stroke-width="1"/>
  </svg>
</section>

<footer class="site-footer">
  <h3 class="footer-title" style="left:199px">Contact <span>Info</span></h3>
  <div class="contact-line" style="top:82px;font-size:14px;text-decoration:underline">
    <svg width="18" height="18" viewBox="0 0 24 24" fill="none" stroke="#fff" stroke-width="1.5"><path d="M5 3h4l2 5-3 2a11 11 0 0 0 6 6l2-3 5 2v4a2 2 0 0 1-2 2A17 17 0 0 1 3 5a2 2 0 0 1 2-2z"/></svg>(603) 555-0172
  </div>
  <div class="contact-line" style="top:113px">
    <svg width="18" height="16" viewBox="0 0 24 20" fill="none" stroke="#fff" stroke-width="1.5"><rect x="2" y="2" width="20" height="16" rx="2"/><path d="M2 4l10 7 10-7"/></svg>info@veltaro-example.com
  </div>
  <div class="contact-line" style="top:141px">
    <svg width="18" height="18" viewBox="0 0 24 24" fill="none" stroke="#fff" stroke-width="1.5"><path d="M12 21s-7-7-7-12a7 7 0 0 1 14 0c0 5-7 12-7 12z"/><circle cx="12" cy="9" r="2.5"/></svg>5280 Lorem Ipsum Park Drive<br>Lorem Ipsum, AB 12345
  </div>
  <span class="abs" style="left:199px;top:194px;font-size:8.5px;font-weight:600;letter-spacing:.8px">FOLLOW US:</span>
  <span class="social" style="left:268px;top:184px" aria-label="Social link"></span>
  <span class="social active" style="left:303px;top:184px" aria-label="Social link"></span>
  <span class="social" style="left:338px;top:184px" aria-label="Social link"></span>
  <span class="social" style="left:373px;top:184px" aria-label="Social link"></span>

  <h3 class="footer-title" style="left:472px">Quick <span>Links</span></h3>
  <ul class="footer-links">
    <li><a class="current" href="#">Home</a></li>
    <li><a href="#">About Us</a></li>
    <li><a href="#">Solutions</a></li>
    <li><a href="#">Our Services</a></li>
    <li><a href="#">Facilities We Serve</a></li>
    <li><a href="#">Industry Associations</a></li>
    <li><a href="#">Contact Us</a></li>
  </ul>

  <h3 class="footer-title" style="left:665px">Inquiry <span>Now!</span></h3>
  <div class="field" style="left:666px;top:81px;width:160px;height:29px">Full Name</div>
  <div class="field" style="left:840px;top:81px;width:160px;height:29px">Email Address</div>
  <div class="field" style="left:666px;top:125px;width:334px;height:61px">Message...</div>
  <a class="submit" href="#">Submit</a>

  <div class="copyright">Copyright © 2025 <u>Veltaro</u>. All Rights Reserved</div>
</footer>

</body>
</html>
```